I need a business card for ALVA Holdings. We are a young startup based in New Zealand working in internet marketing and web development. The design should have some element connected to New Zealand, such as wave, koru or silver fern, just don't use a kiwi bird.

```html
<!DOCTYPE html>
<html lang="en">
<head>
<meta charset="utf-8">
<title>ALVA Holdings – Business Card</title>
<link rel="stylesheet" href="https://fonts.googleapis.com/css2?family=Montserrat:wght@700&family=Open+Sans:ital,wght@1,400&family=Roboto:ital,wght@0,400;0,700;1,300&display=swap">
<style>
  :root {
    --page-bg: #ffffff;
    --brand-blue: #1670b8;
    --card-back-bg: #e0612f;
    --koru-tone: #c9521f;
    --koru-deep: #b8481a;
    --front-bg: #e9e9ec;
    --fern-tone: #c7ccc5;
    --fern-deep: #b6bcb4;
    --leaf-warm: #ddd3c4;
    --card-edge: #c8c8c8;
    --label-blue: #1a74b8;
    --white: #ffffff;
  }
  html, body {
    margin: 0;
    padding: 0;
    overflow: hidden;
    background: var(--page-bg);
  }
  .canvas {
    position: relative;
    width: 1200px;
    height: 1200px;
    overflow: hidden;
    background: var(--page-bg);
  }
  .side-label {
    position: absolute;
    left: 253px;
    width: 687px;
    text-align: center;
    font-family: "Open Sans", sans-serif;
    font-style: italic;
    font-size: 19px;
    color: var(--label-blue);
    margin: 0;
  }
  .side-label--front { top: 141px; }
  .side-label--back { top: 1027px; }

  .card {
    position: absolute;
    left: 253px;
    width: 687px;
    height: 411px;
    overflow: hidden;
    box-sizing: border-box;
  }
  .card--front {
    top: 173px;
    border: 1px solid var(--card-edge);
    background: var(--front-bg);
  }
  .card--back {
    top: 600px;
    height: 412px;
    background: var(--card-back-bg);
    color: var(--white);
  }

  /* Faded silver fern photograph behind the name */
  .fern-photo {
    position: absolute;
    inset: 0;
    background:
      radial-gradient(ellipse 32% 14% at 22% 18%, var(--fern-deep), transparent 75%),
      radial-gradient(ellipse 40% 12% at 45% 8%, var(--fern-tone), transparent 75%),
      radial-gradient(ellipse 18% 10% at 78% 12%, var(--leaf-warm), transparent 75%),
      radial-gradient(ellipse 30% 22% at 86% 80%, var(--fern-deep), transparent 75%),
      radial-gradient(ellipse 24% 18% at 12% 70%, var(--fern-tone), transparent 75%),
      linear-gradient(160deg, #dfe1df 0%, var(--front-bg) 45%, #dcdedb 100%);
  }

  .wordmark {
    position: absolute;
    left: 0;
    right: 0;
    top: 112px;
    text-align: center;
    font-family: "Montserrat", sans-serif;
    font-weight: 700;
    color: var(--brand-blue);
  }
  .wordmark__row {
    display: inline-flex;
    align-items: center;
    gap: 18px;
  }
  .wordmark__dot {
    width: 34px;
    height: 34px;
    border-radius: 50%;
    background: var(--brand-blue);
  }
  .wordmark__name {
    display: block;
    font-size: 158px;
    line-height: 130px;
    letter-spacing: 2px;
  }
  .wordmark__sub {
    display: block;
    margin-top: 22px;
    font-size: 40px;
    line-height: 40px;
    letter-spacing: 26px;
    padding-left: 26px;
  }

  /* Faint koru (unfurling fern frond) photograph, lower left of the back */
  .koru-photo {
    position: absolute;
    left: 44px;
    top: 160px;
    width: 176px;
    height: 252px;
    background:
      radial-gradient(circle at 46% 30%, var(--koru-deep) 0, var(--koru-tone) 26%, transparent 36%),
      radial-gradient(ellipse 22% 30% at 30% 62%, var(--koru-tone), transparent 80%),
      radial-gradient(ellipse 20% 10% at 62% 88%, var(--koru-tone), transparent 85%);
  }

  .contact-name {
    position: absolute;
    left: 0;
    right: 0;
    top: 88px;
    margin: 0;
    text-align: center;
    font-family: "Roboto", sans-serif;
    font-weight: 700;
    font-size: 78px;
    line-height: 80px;
  }
  .contact-role {
    position: absolute;
    left: 0;
    right: 0;
    top: 163px;
    margin: 0;
    text-align: center;
    font-family: "Roboto", sans-serif;
    font-weight: 300;
    font-style: italic;
    font-size: 33px;
    line-height: 38px;
  }
  .contact-list {
    position: absolute;
    left: 0;
    right: 0;
    top: 276px;
    margin: 0;
    padding: 0;
    list-style: none;
    text-align: center;
    font-family: "Roboto", sans-serif;
    font-size: 19px;
    line-height: 23px;
  }
  .contact-list li {
    display: flex;
    justify-content: center;
    align-items: center;
    gap: 10px;
  }
  .contact-list .contact-web { margin-top: 12px; }
  .contact-icon {
    width: 18px;
    height: 18px;
    fill: var(--white);
  }
</style>
</head>
<body>
<main class="canvas">
  <p class="side-label side-label--front">front</p>

  <section class="card card--front" aria-label="Card front">
    <div class="fern-photo" role="img" aria-label="Faded photograph of New Zealand silver fern fronds across the card"></div>
    <div class="wordmark">
      <span class="wordmark__row">
        <span class="wordmark__name">ALVA</span>
        <span class="wordmark__dot"></span>
      </span>
      <span class="wordmark__sub">HOLDINGS</span>
    </div>
  </section>

  <section class="card card--back" aria-label="Card back">
    <div class="koru-photo" role="img" aria-label="Faint photograph of an unfurling New Zealand koru fern frond"></div>
    <h1 class="contact-name">Rowan Hale</h1>
    <p class="contact-role">company position</p>
    <ul class="contact-list">
      <li>
        <svg class="contact-icon" viewBox="0 0 24 24" aria-hidden="true">
          <path d="M6.6 10.8c1.4 2.8 3.8 5.1 6.6 6.6l2.2-2.2c.3-.3.7-.4 1-.2 1.1.4 2.3.6 3.6.6.6 0 1 .4 1 1V20c0 .6-.4 1-1 1C10.6 21 3 13.4 3 4c0-.6.4-1 1-1h3.5c.6 0 1 .4 1 1 0 1.3.2 2.5.6 3.6.1.3 0 .7-.2 1l-2.3 2.2z"/>
        </svg>
        <span>0800-372915</span>
      </li>
      <li>
        <svg class="contact-icon" viewBox="0 0 24 24" aria-hidden="true">
          <path d="M2 5h20v14H2z M3.5 6.5v.3l8.5 6 8.5-6v-.3z" fill-rule="evenodd"/>
        </svg>
        <span>rowanhale@alvaholdings.com</span>
      </li>
      <li class="contact-web"><span>www.alvaholdings.com</span></li>
    </ul>
  </section>

  <p class="side-label side-label--back">back</p>
</main>
</body>
</html>
```